REVISED : Logo & Stationery design for Naturopath

1. I need a logo and stationery (A4 letterhead, Business card & postcard size card for voucher/birthday/reminder use) for my new clinic. 
2. Overall look / logo needs to achieve: sense of personal attention (handwriting like script use somewhere), be unfussy, elegant, professional, modern. calm.
3. MUST be DIFFERENT to what we normally see for naturopaths.
4. Logo will be used eventually on new website so must lend itself to that use.
5. Possible tag lines 'Health is in your nature' or 'Wellbeing at Every Age' = general themes
6. Should appeal to men, mothers, women, depressed, families
Please feel free to submit logo designs prior to stationery work up if preferred.  

Thanks for your designs.  I have updated my brief a little, I hope that it now gives a clearer picture of what I'm looking for.  Have a great day! Marion

Hi Everyone.  I have uploaded some dandelion to give you an idea of the symmetry, perfection and airiness that I'm looking for.

heading away for a week, so apologies to extend the deadline.  Decision will be made on Friday.  Thanks for your patience.

My clients are aged from 5m to 75 years and have an array of problems. My main interest is joint and general inflammation and the role of genetic heritage and nutrigenomics. I follow an evidence based approach. Have a look at www.marionkestle.com.au

Must have
1. some script based font 
2.  colours of nature . 
3. Trading Name: Marion Kestle Naturopathy 
4. Company Name: Brightwell Stride Partners Pty Ltd ABN: 58 217 630 914 (these must be on for legal reasons but not form part of logo or overall company name. 
5. Mailing Address: PO Box 4392, Tallow Ridge NSW 1590 
6. Clinic Address: TBC 
7. Tel: 1300 48 29 63 
8. e: naturopathy@marionkestle.com.au 
9. w: marionkestle.com.au
Business Card and Postcard do not need ABN & Pty Ltd name.
Business Card should have my qualifications: Bachelor of Health Science (Complementary Medicine), ND.
Nice to have
1. design able to be embossed (card, business card)
2. able to be used on non-bleached recycled paper 
3. suitable of matt / uncoated card
4. good for vegetable dye printing
5. concept I really like is of a dandelion blowing in the wind (themes = herb, wistful, dissemination of information, free and easy) 
6. also really like idea of a 'tree of life'
7. but your interpretation of something entirely different might be a winner
8. Use of either of the tag lines 
9. Monochromatic 
Should not have
1. photos
2. more than 3 colours
3. Leaves (too much like every other Naturopath)

```html
<!DOCTYPE html>
<html lang="en">
<head>
<meta charset="utf-8">
<title>Marion Kestle Naturopathy – Letterhead</title>
<link rel="stylesheet" href="https://fonts.googleapis.com/css2?family=Open+Sans:wght@300;400&family=Great+Vibes&display=swap">
<style>
  :root {
    --paper: #ffffff;
    --ink: #1e1e1e;
    --olive: #a8a535;
    --olive-soft: #cfcc7a;
    --footer-text: #e4e3b4;
    --tagline: #c9c77d;
    --signature-tone: #eeeeee;
  }
  html, body {
    margin: 0;
    padding: 0;
    overflow: hidden;
    background: var(--paper);
  }
  .letterhead {
    position: relative;
    width: 849px;
    height: 1200px;
    overflow: hidden;
    background: var(--paper);
    font-family: "Open Sans", Arial, sans-serif;
    color: var(--ink);
  }
  .brand {
    position: absolute;
    top: 34px;
    left: 641px;
    display: flex;
    align-items: flex-start;
    gap: 10px;
  }
  .brand-name {
    margin: 0;
    font-family: "Open Sans", Arial, sans-serif;
    font-weight: 300;
    color: var(--olive);
    font-size: 33px;
    line-height: 34px;
    letter-spacing: -0.5px;
  }
  .brand-name .brand-trade {
    display: block;
    font-size: 20px;
    line-height: 30px;
    letter-spacing: 0.3px;
  }
  .brand-mark {
    width: 34px;
    height: 34px;
    border-radius: 50%;
    background: var(--olive-soft);
    margin-top: 4px;
  }
  .letter {
    position: absolute;
    left: 104px;
    top: 190px;
    width: 690px;
    font-size: 15px;
    line-height: 22px;
  }
  .letter p {
    margin: 0 0 22px;
  }
  .letter .date { margin-bottom: 16px; }
  .letter .recipient { margin-bottom: 31px; }
  .letter .salutation { margin-bottom: 20px; }
  .letter .body-copy { margin-bottom: 23px; white-space: nowrap; }
  .letter .closing { margin-bottom: 6px; }
  .signature {
    display: block;
    width: 100px;
    height: 88px;
    margin-left: -20px;
    margin-bottom: 14px;
    background: linear-gradient(135deg, var(--signature-tone), #fafafa);
  }
  .letter .sender { margin-bottom: 14px; }
  .letter .reference { font-size: 12px; letter-spacing: 0.3px; }
  .footer-band {
    position: absolute;
    left: 0;
    top: 1097px;
    width: 849px;
    height: 103px;
    background: var(--olive);
  }
  .footer-details {
    position: absolute;
    left: 107px;
    top: 2px;
    margin: 0;
    font-size: 9px;
    line-height: 16px;
    color: var(--footer-text);
    font-style: normal;
  }
  .footer-details .label { font-weight: 400; }
  .tagline {
    position: absolute;
    left: 534px;
    top: 22px;
    margin: 0;
    font-family: "Great Vibes", cursive;
    font-size: 30px;
    color: var(--tagline);
    letter-spacing: 1.5px;
  }
</style>
</head>
<body>
<div class="letterhead">
  <header class="brand">
    <h1 class="brand-name">Marion<br>Kestle<span class="brand-trade">Naturopathy</span></h1>
    <span class="brand-mark" aria-hidden="true"></span>
  </header>

  <main class="letter">
    <p class="date">13th July, 2009</p>
    <p class="recipient">27 Larkspur Lane, Fernhaven<br>Sydney, NSW, 2417</p>
    <p class="salutation">Dear Mrs Avery,</p>
    <p class="body-copy">Pat illaorerit verci tatuercilis alit, quat. Xercilit ea feu feuguer augiamet, sed exer inci ea<br>feugue do cor aliquis atismod dolesen iamcon hendio conulput velestion utpatin exercin<br>vendrerostin velit el dolumsa ndigna core dolum do do od magnit utpation ea feummy<br>nullam ver si tisit ut et nonsequat, sim ipsum qui esed tin etueros nonseniat<br>ut amet, veliquat.</p>
    <p class="body-copy">Ipsumsan endre tem iustisl del dolenim velisim in vel ut eugait acipit nonsenim volor atuer se<br>dolutpat, qui ex ex ent aliquis dolortis dio et lore tat am, quam eugait iril delenis modigni<br>smod ercilis et lore exer ip eum dolum velit wiscin eliquismolum iuscilit ing ex ex euguero<br>odiamco nsequam consed dolor ilis esectet accumsan utat am nisi tin utat, conulla orercilla<br>feuip et velis el ing ea feuis at. Do delit nulla feum veriureet aliquate consectet la faccum in<br>utpat. Igna acipis elit pratet vel ulla feugueros dolorti smodolo boreros diat.</p>
    <p class="body-copy">Bor sum dolore tinci tionseq uatisl ullutat erostin hent lorper se corperatis dolummy<br>nulputpate magnibh eniam vendigna autem vel ulput et nullametum nulluptat aliquipsum<br>ipit augiat. Os nos ad modolore modolent velis doloborperit etummodio odolenim iriureetue<br>dolobor ing essit nos at. Ut alisl iliquisim amcorper senis ad te consed etum nostrud delis essit<br>ut wis do od exer sum niam veliscidunt aut irit praessed tem alit augiame tuerili quipit il ulla<br>ad tie tat delisis euisi bla coreet diam, conummy nos aliqui exerat.</p>
    <p class="closing">Yours Faithfully</p>
    <span class="signature" role="img" aria-label="Handwritten signature of Marion Kestle"></span>
    <p class="sender">Marion Kestle<br>Naturopath</p>
    <p class="reference">xxxxxxxxxxxxxxxxxx</p>
  </main>

  <footer class="footer-band">
    <address class="footer-details">
      Brightwell Stride Partners Pty Ltd ABN: 58 217 630 914<br>
      PO Box 4392, Tallow Ridge NSW 1590 &nbsp;&nbsp; <span class="label">t:</span> 1300 48 29 63<br>
      <span class="label">e:</span> naturopathy@marionkestle.com.au &nbsp;&nbsp; <span class="label">w:</span> marionkestle.com.au
    </address>
    <p class="tagline">Wellbeing at Every Age</p>
  </footer>
</div>
</body>
</html>
```